Pitch Deck Powerpoint Template for Entrepreneurship/Education Based Nonprofit

I need a stylish powerpoint design for a start-up nonprofit called Bright Venture Works (BVW). I am building BVWs pitch deck to raise money. BVW is an entrepreneurial incubator and accelerator that seeks to identify, validate, test, and launch innovative ventures that improve public education. An example of our model, and one of our partners, is Nine Oaks Learning in New Orleans and New York :http://nineoakslearn.example

We need the deck to look sleek and innovative - like a start-up pitch deck. Lots of different templates and fonts that pop off the page.

Target Market(s)

Individuals, foundations, and any other stakeholder - we are pitching a new business model and asking for money.

Industry/Entity Type

Building

Font styles to use
Sans Serif

Requirements
Must have
• A sleek/modern feel with several different template slides. charts and graphs/ strong fonts that pop off the page, use of the logo:
• It would be great to have a slide describing the 3 primary programs at Bright Venture Works (BVW):
• - BVWspark - come in with an idea for an innovation in education, and we will do a two day workshop to examine your business assumptions and discuss next steps.
• - BVWpropel - take your idea to a prototype and launch to customers - we help you with an intensive 30 day program
• - BVWnurture - for existing nonprofit projects, we allow you to work under our umbrella to launch and build capacity
• Slides: Problem Definition, Solution, Value Proposition, Data/MEasurement, Key Partners, About the founder, Key Advisors

```html
<!DOCTYPE html>
<html lang="en">
<head>
<meta charset="utf-8">
<title>Problem Definition</title>
<link href="https://fonts.googleapis.com/css2?family=Open+Sans:wght@400;600;700&family=Roboto+Condensed:wght@400&display=swap" rel="stylesheet">
<style>
  :root {
    --stage: #000000;
    --paper: #ffffff;
    --navy: #004279;
    --wave-line: #003d70;
    --magenta: #a92190;
    --purple: #66308f;
    --green: #5a8e0e;
    --orange: #f15b24;
    --sky: #22a8f1;
    --ink: #1a1a1a;
    --page-no: #0a3f79;
  }
  * { margin: 0; padding: 0; box-sizing: border-box; }
  html, body { width: 1200px; height: 1100px; overflow: hidden; background: var(--stage); }
  .canvas { position: relative; width: 1200px; height: 1100px; font-family: "Open Sans", sans-serif; }
  .deck-title {
    position: absolute; top: 94px; left: 0; width: 1230px; text-align: center;
    color: var(--paper); font-weight: 600; font-size: 32px;
  }
  .slide { position: absolute; left: 88px; top: 166px; width: 1024px; height: 768px; background: var(--paper); overflow: hidden; }
  .slide-art { position: absolute; left: 0; top: 0; }
  .header-band {
    position: absolute; left: 0; top: 43px; width: 732px; height: 93px; background: var(--navy);
    color: var(--paper); font-family: "Roboto Condensed", sans-serif; font-size: 46px;
    line-height: 93px; padding-left: 33px; letter-spacing: -0.5px;
  }
  .brand-name {
    position: absolute; left: 760px; top: 50px; color: var(--navy);
    font-weight: 700; font-size: 30px; line-height: 30px;
  }
  .problem { position: absolute; width: 273px; }
  .problem h2 {
    font-family: "Roboto Condensed", sans-serif; font-weight: 400; font-size: 28px;
    letter-spacing: -0.8px; line-height: 1; margin-bottom: 22px; white-space: nowrap;
  }
  .problem p { color: var(--ink); font-size: 16px; line-height: 21.6px; text-align: justify; }
  .p1 { left: 32px; top: 178px; } .p1 h2 { color: var(--purple); }
  .p2 { left: 723px; top: 173px; } .p2 h2 { color: var(--green); margin-left: 3px; margin-bottom: 27px; }
  .p3 { left: 32px; top: 454px; } .p3 h2 { color: var(--orange); }
  .p4 { left: 723px; top: 448px; } .p4 h2 { color: var(--sky); margin-left: 14px; }
  .slice-label { font-family: "Open Sans", sans-serif; font-size: 24px; fill: var(--paper); }
  .footer-text {
    position: absolute; top: 716px; color: var(--paper); font-weight: 700; font-size: 24px;
  }
  .page-label { left: 45px; }
  .site-label { right: 54px; }
  .deck-page {
    position: absolute; right: 22px; bottom: 14px; color: var(--page-no); font-size: 32px;
  }
</style>
</head>
<body>
<div class="canvas">
  <div class="deck-title">Problem Defination</div>

  <section class="slide">
    <svg class="slide-art" width="1024" height="768" viewBox="0 0 1024 768">
      <defs>
        <pattern id="wave" width="25" height="18" patternUnits="userSpaceOnUse" x="0" y="676">
          <path d="M0 9 Q6.25 1 12.5 9 T25 9 V18 H0 Z" fill="var(--magenta)"/>
          <path d="M0 9 Q6.25 1 12.5 9 T25 9" fill="none" stroke="var(--wave-line)" stroke-width="3"/>
        </pattern>
      </defs>

      <!-- pie chart -->
      <g transform="translate(495 343)">
        <path d="M-2 -2 V-115 A115 115 0 0 0 -115 -2 Z" fill="var(--purple)"/>
        <path d="M2 -2 V-115 A115 115 0 0 1 115 -2 Z" fill="var(--green)"/>
        <path d="M-2 2 H-115 A115 115 0 0 0 -2 115 Z" fill="var(--orange)"/>
        <path d="M2 2 H115 A115 115 0 0 1 2 115 Z" fill="var(--sky)"/>
        <text class="slice-label" x="-44" y="-32" text-anchor="middle">25%</text>
        <text class="slice-label" x="48" y="-32" text-anchor="middle">25%</text>
        <text class="slice-label" x="-44" y="52" text-anchor="middle">25%</text>
        <text class="slice-label" x="48" y="52" text-anchor="middle">25%</text>
      </g>

      <!-- connectors -->
      <polyline points="252,202 317,202 377,252" fill="none" stroke="var(--purple)" stroke-width="1.2"/>
      <circle cx="377" cy="252" r="5.5" fill="var(--purple)"/>
      <polyline points="594,249 654,199 720,199" fill="none" stroke="var(--green)" stroke-width="1.2"/>
      <circle cx="594" cy="249" r="5.5" fill="var(--green)"/>
      <polyline points="386,427 326,477 260,477" fill="none" stroke="var(--orange)" stroke-width="1.2"/>
      <circle cx="386" cy="427" r="5.5" fill="var(--orange)"/>
      <polyline points="603,423 662,473 730,473" fill="none" stroke="var(--sky)" stroke-width="1.2"/>
      <circle cx="603" cy="423" r="5.5" fill="var(--sky)"/>

      <!-- footer wave -->
      <rect x="0" y="676" width="1024" height="18" fill="url(#wave)"/>
      <rect x="0" y="693" width="1024" height="75" fill="var(--magenta)"/>
    </svg>

    <header class="header-band">PROBLEM DEFINITION</header>
    <div class="brand-name">Bright<br>Venture<br>Works</div>

    <article class="problem p1">
      <h2>PROBLEM DEFINATION 1</h2>
      <p>Lorem ipsum dolor sit amet, consectetuer adipiscing elit, sed diam nonummy nibh euismod tincidunt ut laoreet dolore magna aliquam erat volutpat. Ut wisi enim ad minim veniam, quis nostrud exerci tation ullam.</p>
    </article>
    <article class="problem p2">
      <h2>PROBLEM DEFINATION 2</h2>
      <p>Lorem ipsum dolor sit amet, consectetuer adipiscing elit, sed diam nonummy nibh euismod tincidunt ut laoreet dolore magna aliquam erat volutpat. Ut wisi enim ad minim veniam, quis nostrud exerci tation ullam.</p>
    </article>
    <article class="problem p3">
      <h2>PROBLEM DEFINATION 3</h2>
      <p>Lorem ipsum dolor sit amet, consectetuer adipiscing elit, sed diam nonummy nibh euismod tincidunt ut laoreet dolore magna aliquam erat volutpat. Ut wisi enim ad minim veniam, quis nostrud exerci tation ullam.</p>
    </article>
    <article class="problem p4">
      <h2>PROBLEM DEFINATION 4</h2>
      <p>Lorem ipsum dolor sit amet, consectetuer adipiscing elit, sed diam nonummy nibh euismod tincidunt ut laoreet dolore magna aliquam erat volutpat. Ut wisi enim ad minim veniam, quis nostrud exerci tation ullam.</p>
    </article>

    <div class="footer-text page-label">Page 1</div>
    <div class="footer-text site-label">www.bvw.example</div>
  </section>

  <div class="deck-page">24</div>
</div>
</body>
</html>
```